New solo practice law firm is looking for an elegant, professional, and interactive web design

I need a web design and developer for a new small law firm in Sacramento, California called Dorian Kessly Law, A Professional Corporation. I am a trial lawyer who represents average people facing difficult litigation disputes, including criminal defense as a former prosecutor and civil litigation as a civil litigator. Criminal defense includes domestic violence, battery, assault, drug possession, theft, DUI, etc. Civil litigation includes business disputes, property disputes, employment disputes, family law disputes, and immigration issues. I would like to see web designs that incorporate my logo and use the logo's navy blue and gold colors. I have uploaded the files of my logo to this brief. Please only use the navy blue and gold version. Overall, I want the design to look firm, professional, and elegant.

I plan on having the following pages on my website: (1) Home, (2) Dorian Kessly, (3) Practice Areas, (4) Insights, (5) Contact. I've hand drawn a preliminary sketch concept of what I envision the home page's layout to look like (attached with a text version). I would like your design to keep a similar layout for the homepage and incorporate my logo's colors within it but I am open to creative layout alternatives/ideas. I would like the other pages to have a similar look and feel as the home page. Some of the areas currently in my sketch do not have the full text. You can insert other text for now and I will provide the winner the full text.

In terms of the pictures on the website, I enjoy images of courthouses, columns (example attached but I cannot use this one), and, if possible, images from Sacramento, CA in my background (headshot attached). A plus would be live images that move and also sections of the webpage moving in the viewers view as they scroll down on the page. Also, it would be great to have my logo act as the tab for the website. I can provide other versions of the logo if needed.

I look forward to seeing your Wordpress designs!

People needing legal representation.

Law

Coded - Design and coding required

5+ page

Serif

• Incorporate my logo and my logo's colors.
• Live pictures and images appearing as viewers scroll on page.

```html
<!DOCTYPE html>
<html lang="en">
<head>
<meta charset="utf-8">
<title>Dorian Kessly Law, A Professional Corporation</title>
<link href="https://fonts.googleapis.com/css2?family=Montserrat:wght@600;700&family=Roboto:wght@400;500;700&display=swap" rel="stylesheet">
<style>
:root{
  --navy:#152440;
  --navy-deep:#0f1b33;
  --gold:#8a7442;
  --gold-light:#b89c5e;
  --text:#555b66;
  --heading:#1b2a4a;
  --gray-bg:#f4f4f4;
  --line:#cfcfcf;
  --white:#ffffff;
}
*{margin:0;padding:0;box-sizing:border-box}
html,body{width:1200px;height:2846px;overflow:hidden}
body{font-family:'Roboto',sans-serif;color:var(--text);background:var(--white);position:relative}
.abs{position:absolute}
h1,h2,h3{font-family:'Montserrat',sans-serif;font-weight:700;color:var(--heading)}

/* top bar */
.topbar{top:0;left:0;width:1200px;height:48px;background:var(--navy);color:var(--white);font-size:13px;font-weight:700}
.topbar .item{position:absolute;top:0;height:48px;display:flex;align-items:center;gap:22px}
.topbar .dot{width:32px;height:32px;border-radius:50%;background:var(--white);display:flex;align-items:center;justify-content:center}
.topbar .divider{position:absolute;left:574px;top:6px;width:1px;height:36px;background:#3a4866}
.topbar .cta{position:absolute;left:900px;top:0;width:188px;height:48px;background:var(--gold);display:flex;align-items:center;justify-content:center;font-size:14px}

/* nav */
.nav{top:48px;left:0;width:1200px;height:90px;background:var(--white)}
.nav ul{position:absolute;right:112px;top:0;height:90px;display:flex;align-items:center;gap:23px;list-style:none;font-size:15px;font-weight:700;color:var(--heading)}
.nav li.active{color:var(--gold)}
.nav .caret{display:inline-block;margin-left:6px;vertical-align:middle}
.logo-tab{top:48px;left:81px;width:201px;height:132px;background:var(--white);clip-path:polygon(0 103px,0 0,100% 0,100% 103px,87% 100%,13% 100%);z-index:3;display:flex;flex-direction:column;align-items:center;justify-content:center;gap:9px;padding-bottom:6px}
.logo-tab .mark{width:34px;height:34px;background:var(--navy)}
.logo-tab .name{font-family:'Montserrat',sans-serif;font-weight:700;font-size:13px;color:var(--navy);letter-spacing:1px}
.logo-tab .tag{font-family:'Montserrat',sans-serif;font-weight:600;font-size:6px;color:var(--navy);letter-spacing:1px;margin-top:-6px}

/* hero */
.hero{top:138px;left:0;width:1200px;height:600px;background:linear-gradient(100deg,#0f1830 0%,#27345a 25%,#7a2a1c 48%,#b23a1e 60%,#2a1c1c 80%,#3a2018 100%)}
.hero .portrait{position:absolute;right:0;top:30px;width:420px;height:570px;background:linear-gradient(180deg,rgba(30,30,34,0) 0%,rgba(20,20,24,.55) 40%,rgba(15,15,18,.85) 100%)}
.hero h1{position:absolute;left:110px;top:206px;font-size:48px;line-height:60px;color:var(--white);letter-spacing:.5px}
.hero .sub{position:absolute;left:190px;top:272px;font-family:'Montserrat',sans-serif;font-weight:600;font-size:25px;line-height:30px;color:var(--white)}
.btn{background:var(--gold);color:var(--white);font-weight:700;font-size:14px;display:flex;align-items:center;justify-content:center}
.hero .btn{position:absolute;left:317px;top:335px;width:189px;height:47px}

/* practice */
.practice{top:738px;left:0;width:1200px;height:648px}
.practice h2{position:absolute;top:90px;width:1200px;text-align:center;font-size:27px}
.practice p{position:absolute;left:170px;top:145px;width:860px;text-align:center;font-size:14px;line-height:25px}
.practice .rule{position:absolute;left:553px;top:219px;width:94px;height:3px;background:var(--gold)}
.card{position:absolute;top:260px;width:233px}
.card .photo{width:233px;height:256px}
.card a{display:block;margin-top:14px;text-align:center;font-weight:700;font-size:18px;color:var(--gold);text-decoration:underline}

/* about */
.about{top:1386px;left:0;width:1200px;height:470px}
.about .panel{position:absolute;left:0;top:0;width:600px;height:470px;background:var(--gray-bg)}
.about h2{position:absolute;left:110px;top:46px;font-size:28px;line-height:36px;width:420px}
.about p{position:absolute;left:112px;width:441px;font-size:14.5px;line-height:25px;text-align:justify}
.about .btn{position:absolute;left:112px;top:368px;width:146px;height:47px}
.about .photo{position:absolute;left:600px;top:0;width:600px;height:470px;background:linear-gradient(90deg,#2a2420 0%,#6b5c4c 30%,#a8977f 50%,#5c4c3c 70%,#2c241c 100%)}

/* contact */
.contact{top:1856px;left:0;width:1200px;height:588px}
.contact h2{position:absolute;left:111px;top:94px;font-size:28px;line-height:36px}
.field{position:absolute;left:112px;width:459px;border:1px solid var(--line);background:var(--white);font-size:14px;color:#666;padding:0 14px;display:flex;align-items:center}
.field.area{align-items:flex-start;padding-top:14px}
.contact .submit{position:absolute;left:112px;top:442px;width:459px;height:50px}
.contact h3{position:absolute;left:625px;top:94px;width:470px;font-family:'Roboto',sans-serif;font-size:25px;line-height:36px;font-weight:700}
.circle{position:absolute;left:625px;width:88px;height:88px;border-radius:50%;background:var(--white);box-shadow:0 2px 10px rgba(0,0,0,.15);display:flex;align-items:center;justify-content:center}
.info{position:absolute;left:755px;font-size:19px;line-height:28px;color:#666}

/* footer */
.footer{top:2444px;left:0;width:1200px;height:402px;background:var(--navy);color:var(--white)}
.footer .brand{position:absolute;left:112px;top:120px;display:flex;align-items:center;gap:10px}
.footer .brand .mark{width:14px;height:14px;background:var(--gold)}
.footer .brand span{font-family:'Montserrat',sans-serif;font-weight:600;font-size:19px;letter-spacing:2px;color:var(--gold-light)}
.footer h3{position:absolute;top:48px;color:var(--white);font-family:'Roboto',sans-serif;font-size:21px}
.footer .addr{position:absolute;left:544px;top:103px;font-size:15px;line-height:27px}
.footer .pin{position:absolute;left:495px;top:108px;width:36px;height:36px;border-radius:50%;background:var(--white);display:flex;align-items:center;justify-content:center}
.social{position:absolute;top:178px;width:35px;height:35px;border-radius:50%;border:1.5px solid var(--white)}
.links{position:absolute;left:945px;top:100px;list-style:none;font-size:15.5px}
.links li{height:26.5px;display:flex;align-items:center;gap:22px}
.footer .rule{position:absolute;left:112px;top:283px;width:976px;height:1px;background:#46536e}
.footer .legal{position:absolute;top:306px;width:1200px;text-align:center;font-size:11.5px;line-height:23px}
.footer .copy{position:absolute;top:372px;width:1200px;text-align:center;font-size:12px}
</style>
</head>
<body>

<header class="abs topbar">
  <div class="item" style="left:112px">
    <span class="dot"><svg width="12" height="16" viewBox="0 0 12 16"><path d="M6 0C2.7 0 0 2.6 0 5.8 0 10 6 16 6 16s6-6 6-10.2C12 2.6 9.3 0 6 0z" fill="#8a7442"/><circle cx="6" cy="5.8" r="2.2" fill="#fff"/></svg></span>
    4280 HARBOR POINT WAY SUITE #210 ELK GROVE, CA 95758
  </div>
  <div class="divider"></div>
  <div class="item" style="left:600px">
    <span class="dot"><svg width="15" height="15" viewBox="0 0 24 24"><path d="M6.6 10.8a15.1 15.1 0 0 0 6.6 6.6l2.2-2.2c.3-.3.7-.4 1-.2 1.1.4 2.3.6 3.6.6.6 0 1 .4 1 1V20c0 .6-.4 1-1 1C10.6 21 3 13.4 3 4c0-.6.4-1 1-1h3.5c.6 0 1 .4 1 1 0 1.3.2 2.5.6 3.6.1.3 0 .7-.2 1z" fill="#8a7442"/></svg></span>
    (916) 555-0142
  </div>
  <div class="cta">FREE CONSULTATION</div>
</header>

<nav class="abs nav">
  <ul>
    <li class="active">HOME</li>
    <li>DORIAN KESSLY</li>
    <li>PRACTICE AREAS<svg class="caret" width="10" height="6" viewBox="0 0 10 6"><path d="M1 1l4 4 4-4" stroke="#1b2a4a" stroke-width="1.5" fill="none"/></svg></li>
    <li>INSIGHTS</li>
    <li>CONTACT</li>
    <li style="font-weight:400">|</li>
    <li style="margin-left:-8px">ENG<svg class="caret" width="10" height="6" viewBox="0 0 10 6"><path d="M1 1l4 4 4-4" stroke="#1b2a4a" stroke-width="1.5" fill="none"/></svg></li>
  </ul>
</nav>
<div class="abs logo-tab">
  <i class="mark"></i>
  <span class="name">DORIAN KESSLY LAW</span>
  <span class="tag">A PROFESSIONAL CORPORATION</span>
</div>

<section class="abs hero" role="img" aria-label="Night view of the Sacramento Tower Bridge and city skyline reflected on the river">
  <div class="portrait" role="img" aria-label="Portrait of the attorney in a dark suit and tie"></div>
  <h1>DORIAN KESSLY LAW</h1>
  <div class="sub">A PROFESSIONAL CORPORATION</div>
  <div class="btn">FREE CONSULTATION</div>
</section>

<section class="abs practice">
  <h2>CRIMINAL AND CIVIL TRIAL LAWYERS</h2>
  <p>Dorian Kessly Law is a law firm serving the Sacramento, Yolo, San Joaquin, Solano and Stanislaus Counties. We represent clients in a wide array of criminal, civil, family law, and immigration cases.</p>
  <div class="rule"></div>
  <div class="card" style="left:112px"><div class="photo" role="img" aria-label="Attorney consulting with a client in an orange jumpsuit" style="background:linear-gradient(120deg,#1c1c22 0%,#3a3234 50%,#c24a22 80%,#e3e0dc 100%)"></div><a>CRIMINAL DEFENSE</a></div>
  <div class="card" style="left:359px"><div class="photo" role="img" aria-label="Lawyer in a suit writing notes at a desk" style="background:linear-gradient(160deg,#e8e8e6 0%,#9a9a9c 40%,#2a2a2e 70%,#4a3a30 100%)"></div><a>CIVIL LITIGATION</a></div>
  <div class="card" style="left:607px"><div class="photo" role="img" aria-label="Hands exchanging a document card in a bright office" style="background:linear-gradient(150deg,#3c4a5a 0%,#8a96a4 45%,#e9ddc8 70%,#cfc8c0 100%)"></div><a>IMMIGRATION</a></div>
  <div class="card" style="left:855px"><div class="photo" role="img" aria-label="Couple meeting with a family law advisor" style="background:linear-gradient(160deg,#e3dccf 0%,#c9a88a 45%,#8c7868 70%,#4e6478 100%)"></div><a>FAMILY LAW</a></div>
</section>

<section class="abs about">
  <div class="panel"></div>
  <h2>READY, RELIABLE, AND EXPERIENCED</h2>
  <p style="top:144px">Lorem ipsum dolor sit amet, consectetur adipiscing elit, sed do eiusmod tempor incididunt ut labore et dolore magna aliqua. Ut enim ad minim veniam, quis nostrud exercitation ullamco laboris nisi ut aliquip ex ea commodo consequat.</p>
  <p style="top:260px">Tempor incididunt ut labore et dolore magna aliqua. Ut enim ad minim veniam, quis nostrud exercitation ullamco laboris nisi ut aliquip ex ea commodo consequat.</p>
  <div class="btn">ABOUT DORIAN</div>
  <div class="photo" role="img" aria-label="Courthouse columns with a marble bust and lamp posts"></div>
</section>

<section class="abs contact">
  <h2>SCHEDULE A FREE<br>CONSULTATION</h2>
  <div class="field" style="top:192px;height:44px">Name</div>
  <div class="field" style="top:245px;height:44px">Email</div>
  <div class="field" style="top:295px;height:44px">Phone number</div>
  <div class="field area" style="top:348px;height:87px">Please enter a brief description of your case</div>
  <div class="btn submit">SUBMIT</div>

  <h3>WHEN YOU CONTACT DORIAN KESSLY LAW FOR A FREE CONSULTATION .....</h3>
  <div class="circle" style="top:190px"><svg width="40" height="40" viewBox="0 0 24 24"><path d="M6.6 10.8a15.1 15.1 0 0 0 6.6 6.6l2.2-2.2c.3-.3.7-.4 1-.2 1.1.4 2.3.6 3.6.6.6 0 1 .4 1 1V20c0 .6-.4 1-1 1C10.6 21 3 13.4 3 4c0-.6.4-1 1-1h3.5c.6 0 1 .4 1 1 0 1.3.2 2.5.6 3.6.1.3 0 .7-.2 1z" fill="none" stroke="#8a7442" stroke-width="1.6"/><path d="M14 3.5a7 7 0 0 1 6.5 6.5M14 7a3.5 3.5 0 0 1 3 3" fill="none" stroke="#8a7442" stroke-width="1.6" stroke-linecap="round"/></svg></div>
  <div class="info" style="top:220px">(916) 555-0142</div>
  <div class="circle" style="top:307px"><svg width="40" height="40" viewBox="0 0 24 24"><path d="M12 2a6 6 0 0 0-6 6c0 4.5 6 11 6 11s6-6.5 6-11a6 6 0 0 0-6-6z" fill="none" stroke="#8a7442" stroke-width="1.6"/><circle cx="12" cy="8" r="2.2" fill="none" stroke="#8a7442" stroke-width="1.6"/><ellipse cx="12" cy="20.5" rx="7" ry="1.8" fill="none" stroke="#8a7442" stroke-width="1.6"/></svg></div>
  <div class="info" style="top:310px">4280 HARBOR POINT WAY<br>SUITE #210 ELK GROVE,<br>CA 95758</div>
</section>

<footer class="abs footer">
  <div class="brand"><i class="mark"></i><span>DORIAN KESSLY LAW</span></div>
  <h3 style="left:495px">CONTACT INFO</h3>
  <span class="pin"><svg width="11" height="15" viewBox="0 0 12 16"><path d="M6 0C2.7 0 0 2.6 0 5.8 0 10 6 16 6 16s6-6 6-10.2C12 2.6 9.3 0 6 0z" fill="#8a7442"/><circle cx="6" cy="5.8" r="2.2" fill="#fff"/></svg></span>
  <div class="addr">4280 Harbor Point Way. Suite #210<br>Elk Grove, CA 95758</div>
  <span class="social" style="left:495px" aria-label="Social profile"></span>
  <span class="social" style="left:542px" aria-label="Social profile"></span>
  <span class="social" style="left:590px" aria-label="Social profile"></span>
  <h3 style="left:945px">QUICK LINKS</h3>
  <ul class="links">
    <li><svg width="14" height="14" viewBox="0 0 14 14"><circle cx="7" cy="7" r="7" fill="#9aa3b5"/><path d="M5 4l3 3-3 3" stroke="#152440" stroke-width="1.8" fill="none"/></svg>Home</li>
    <li><svg width="14" height="14" viewBox="0 0 14 14"><circle cx="7" cy="7" r="7" fill="#9aa3b5"/><path d="M5 4l3 3-3 3" stroke="#152440" stroke-width="1.8" fill="none"/></svg>Dorian Kessly</li>
    <li><svg width="14" height="14" viewBox="0 0 14 14"><circle cx="7" cy="7" r="7" fill="#9aa3b5"/><path d="M5 4l3 3-3 3" stroke="#152440" stroke-width="1.8" fill="none"/></svg>Practice Areas</li>
    <li><svg width="14" height="14" viewBox="0 0 14 14"><circle cx="7" cy="7" r="7" fill="#9aa3b5"/><path d="M5 4l3 3-3 3" stroke="#152440" stroke-width="1.8" fill="none"/></svg>Insights</li>
    <li><svg width="14" height="14" viewBox="0 0 14 14"><circle cx="7" cy="7" r="7" fill="#9aa3b5"/><path d="M5 4l3 3-3 3" stroke="#152440" stroke-width="1.8" fill="none"/></svg>Contact</li>
    <li><svg width="14" height="14" viewBox="0 0 14 14"><circle cx="7" cy="7" r="7" fill="#9aa3b5"/><path d="M5 4l3 3-3 3" stroke="#152440" stroke-width="1.8" fill="none"/></svg>Privacy Policy</li>
  </ul>
  <div class="rule"></div>
  <p class="legal">The information on this website is for general information purposes only. Nothing on this site should be taken as legal advice for any individual case or situation.<br>This information is not intended to create, and receipt of viewing does not constitute an attorney-client relationship.</p>
  <p class="copy">Copyright 2021 All Rights Reserved</p>
</footer>

</body>
</html>
```